Business Card and Word .doc header and footer required

I need a business card designed for my cybersecurity consulting company. Also required, is a header and footer to be ued for my word documents.
Attached is the Logo design, font and rgb used.

Industry/Entity Type

Cyber Security Consulting

Contact Information for Business Card

Name, Phone, email, website

Colors
0054AA
0677BA
7BADD7
CADEEF
E8F1F8

Requirements
Must have
• Sleek, modern

```html
<!DOCTYPE html>
<html lang="en">
<head>
<meta charset="utf-8">
<title>Harlow Ridge Consulting – Stationery</title>
<link rel="stylesheet" href="https://fonts.googleapis.com/css2?family=Montserrat:wght@600;700&family=Lato:wght@400;700&display=swap">
<style>
  :root {
    --navy: #17243a;
    --ink: #111822;
    --slate-blue: #5b80ab;
    --royal: #0677ba;
    --deep-blue: #0054aa;
    --sky: #7badd7;
    --silver: #d9dee4;
    --paper: #ffffff;
    --text-dark: #1a1a1a;
    --shadow: 0 6px 14px rgba(0,0,0,.28);
  }
  * { margin: 0; padding: 0; box-sizing: border-box; }
  html, body { width: 1200px; height: 900px; overflow: hidden; background: var(--paper); }
  body { position: relative; font-family: "Lato", sans-serif; }

  .card, .letterhead { position: absolute; background: var(--paper); box-shadow: var(--shadow); overflow: hidden; }

  /* Card front */
  .card--front { left: 114px; top: 152px; width: 514px; height: 293px; }
  .card__brand-panel { position: absolute; left: 0; top: 0; width: 247px; height: 100%; background: var(--navy); }
  .card__name-band { position: absolute; left: 235px; top: 45px; width: 279px; height: 56px; background: var(--slate-blue); }
  .card__name-fold { position: absolute; left: 235px; top: 101px; }
  .card__name { position: absolute; left: 308px; top: 56px; color: var(--paper); font: 700 20px/1 "Lato", sans-serif; letter-spacing: -.2px; white-space: nowrap; }
  .card__role { position: absolute; left: 308px; top: 80px; color: var(--paper); font: 400 12px/1 "Lato", sans-serif; white-space: nowrap; }
  .contact { position: absolute; left: 267px; display: flex; align-items: center; gap: 14px; color: var(--slate-blue); font-size: 12px; white-space: nowrap; }
  .contact svg { width: 27px; height: 27px; flex: none; }
  .contact--phone { top: 143px; }
  .contact--mail { top: 187px; }
  .contact--web { top: 231px; }

  /* Brand lockup */
  .brand { position: absolute; text-align: center; font-family: "Montserrat", sans-serif; font-weight: 700; }
  .brand__dot { display: block; margin: 0 auto; border-radius: 50%; }
  .brand__name { display: block; white-space: nowrap; line-height: 1; }
  .brand__tag { display: block; letter-spacing: .3em; line-height: 1; white-space: nowrap; }

  .brand--front { left: 0; top: 82px; width: 247px; color: var(--silver); }
  .brand--front .brand__dot { width: 64px; height: 64px; border: 4px solid var(--slate-blue); margin-bottom: 22px; }
  .brand--front .brand__name { font-size: 23px; }
  .brand--front .brand__tag { font-size: 11px; margin-top: 6px; }

  /* Card back */
  .card--back { left: 114px; top: 454px; width: 514px; height: 294px; }
  .card__dark { position: absolute; left: 0; top: 0; width: 100%; height: 226px; background: var(--ink); }
  .card__stripe { position: absolute; left: 0; top: 226px; width: 100%; height: 8px; background: var(--royal); }
  .card__web { position: absolute; left: 0; top: 244px; width: 100%; text-align: center; color: var(--text-dark); font-size: 16px; }
  .brand--back { left: 0; top: 64px; width: 514px; color: var(--silver); }
  .brand--back .brand__dot { width: 70px; height: 70px; border: 4px solid var(--slate-blue); margin-bottom: 22px; }
  .brand--back .brand__name { font-size: 25px; }
  .brand--back .brand__tag { font-size: 11px; margin-top: 7px; }

  /* Letterhead */
  .letterhead { left: 695px; top: 152px; width: 423px; height: 596px; border-left: 1px solid var(--deep-blue); border-right: 1px solid var(--deep-blue); }
  .letterhead__mark { position: absolute; left: 65px; top: 24px; width: 46px; height: 46px; border-radius: 50%; border: 3px solid #ececec; }
  .brand--header { left: 137px; top: 43px; color: var(--royal); }
  .brand--header .brand__name { font-size: 19px; }
  .brand--header .brand__tag { font-size: 8px; margin-top: 4px; }
  .brand--footer { left: 154px; top: 515px; width: 120px; color: var(--deep-blue); }
  .brand--footer .brand__dot { width: 22px; height: 22px; border: 2px solid var(--royal); margin-bottom: 6px; }
  .brand--footer .brand__name { font-size: 8px; }
  .brand--footer .brand__tag { font-size: 4px; margin-top: 2px; }
</style>
</head>
<body>

  <section class="card card--front" aria-label="Business card front">
    <div class="card__brand-panel">
      <div class="brand brand--front">
        <span class="brand__dot"></span>
        <span class="brand__name">HARLOW RIDGE</span>
        <span class="brand__tag">CONSULTING</span>
      </div>
    </div>
    <div class="card__name-band"></div>
    <svg class="card__name-fold" width="12" height="10" viewBox="0 0 12 10"><polygon points="0,0 12,0 12,10" fill="#3c5779"/></svg>
    <div class="card__name">YOUR NAME</div>
    <div class="card__role">MANAGER</div>

    <div class="contact contact--phone">
      <svg viewBox="0 0 28 28" fill="none" stroke="#5b80ab" stroke-width="1.6"><circle cx="14" cy="14" r="12.5"/><path d="M10.5 8.5l2 3-1.3 1.3c.7 1.6 1.9 2.8 3.5 3.5l1.3-1.3 3 2-1.2 2c-4.5-.3-8.8-4.6-9.1-9.1z" stroke-linejoin="round"/></svg>
      <span>+ 333 333 3333</span>
    </div>
    <div class="contact contact--mail">
      <svg viewBox="0 0 28 28" fill="none" stroke="#5b80ab" stroke-width="1.6"><circle cx="14" cy="14" r="12.5"/><rect x="7.5" y="9.5" width="13" height="9"/><path d="M7.5 9.5l6.5 5 6.5-5M7.5 18.5l5-4.2M20.5 18.5l-5-4.2"/></svg>
      <span>yourmail@mailbox.com</span>
    </div>
    <div class="contact contact--web">
      <svg viewBox="0 0 28 28" fill="none" stroke="#5b80ab" stroke-width="1.4"><circle cx="14" cy="14" r="12.5"/><circle cx="14" cy="14" r="7.5"/><ellipse cx="14" cy="14" rx="3.3" ry="7.5"/><path d="M6.5 14h15M7.5 10.5h13M7.5 17.5h13M14 6.5v15"/></svg>
      <span>www.yourweb.com</span>
    </div>
  </section>

  <section class="card card--back" aria-label="Business card back">
    <div class="card__dark">
      <div class="brand brand--back">
        <span class="brand__dot"></span>
        <span class="brand__name">HARLOW RIDGE</span>
        <span class="brand__tag">CONSULTING</span>
      </div>
    </div>
    <div class="card__stripe"></div>
    <div class="card__web">www.yourweb.com</div>
  </section>

  <section class="letterhead" aria-label="Document header and footer">
    <span class="letterhead__mark"></span>
    <div class="brand brand--header">
      <span class="brand__name">HARLOW RIDGE</span>
      <span class="brand__tag">CONSULTING</span>
    </div>
    <div class="brand brand--footer">
      <span class="brand__dot"></span>
      <span class="brand__name">HARLOW RIDGE</span>
      <span class="brand__tag">CONSULTING</span>
    </div>
  </section>

</body>
</html>
```